Homepage Redesign - Hi-tech business Law Firm

I'm looking for an updated graphic design (pdf file) for the homepage of dorvantlegal.ca (and which will form the general template of the other pages - but you don't need to design that). Detailed specs are in the Word file.

Deliverable is 1 pdf file that I find good looking, that sets forth the layout of the new page.

Target Market(s)

Sophisticated customers

Industry/Entity Type

Legal

Number of Pages Required

1 page

Requirements
Nice to have
• For a main background, tech type images to do with high powered boardrooms, computers, graphs, numbers, high tech manufacturing lines etc. Also, I tend to like blues and light greys, and uploaded a file today that shows my generally preferred layout, which a few of you have been getting close to.
Should not have
• Any mention of 'Personal Injury,' backgrounds that include books, or buildings with roman columns. Page should not be in dark colors or harsh on the eyes.

```html
<!DOCTYPE html>
<html lang="en">
<head>
<meta charset="utf-8">
<title>Dorvant Law Firm — Business Litigation Lawyers</title>
<link href="https://fonts.googleapis.com/css2?family=Libre+Baskerville:wght@400;700&family=Tinos:wght@400;700&display=swap" rel="stylesheet">
<style>
:root{
  --navy:#0c4f71;
  --navy-deep:#0b3954;
  --steel:#4a7f99;
  --ink:#2a2a2a;
  --muted:#8a8a8a;
  --grey:#e9e9e9;
  --light:#f4f4f4;
  --white:#ffffff;
  --head:'Libre Baskerville', Georgia, serif;
  --body:'Tinos', 'Times New Roman', serif;
}
*{box-sizing:border-box;margin:0;padding:0}
html,body{width:1200px;height:3724px;overflow:hidden}
body{position:relative;font-family:var(--body);color:var(--ink);background:var(--white)}
.abs{position:absolute}
svg{display:block}

/* top bar */
.topbar{left:0;top:0;width:1200px;height:32px;background:var(--navy);color:#fff;font-size:12px}
.topbar .contact{left:150px;top:9px;display:flex;gap:20px}
.topbar .contact span{display:flex;align-items:center;gap:6px}
.topbar .region{left:523px;top:9px;letter-spacing:.5px}
.topbar .search{left:1028px;top:6px;width:21px;height:21px;background:#2b6f92;border-radius:3px;display:flex;align-items:center;justify-content:center}

/* header */
.header{left:0;top:32px;width:1200px;height:78px;background:#fff}
.brand{left:150px;top:12px;display:flex;align-items:center;gap:8px}
.brand .mark{width:34px;height:34px;border:2px solid var(--navy-deep);flex:none}
.brand .name{font-family:var(--head);font-size:13px;letter-spacing:3px;color:var(--navy-deep);line-height:1.2;white-space:nowrap}
.tagline{left:150px;top:55px;font-size:9px;font-style:italic;color:#444}
.nav{left:421px;top:32px;display:flex;gap:24px;font-family:var(--body);font-size:12.5px;color:#333;white-space:nowrap}
.nav .active{color:var(--navy);text-decoration:underline}
.cta-btn{left:865px;top:24px;width:185px;height:29px;background:var(--navy);color:#fff;font-family:var(--body);font-size:12px;display:flex;align-items:center;justify-content:center;border-radius:2px}

/* hero */
.hero{left:0;top:110px;width:1200px;height:434px;background:radial-gradient(ellipse at 80% 45%,#6b4a34 0%,#3d2a1f 45%,#1f1611 100%)}
.hero-portrait{left:660px;top:0;width:540px;height:434px;background:linear-gradient(180deg,#5a4436 0%,#2a2422 60%,#1a1a1d 100%)}
.hero h1{left:150px;top:102px;font-family:var(--head);font-weight:700;color:#fff;font-size:30px;line-height:42px;letter-spacing:.5px}
.btn{display:flex;align-items:center;justify-content:center;font-family:var(--body);font-size:12px;color:#fff;border-radius:2px}
.hero .read{left:150px;top:295px;width:111px;height:29px;background:var(--navy)}
.hero .video{left:270px;top:295px;width:130px;height:29px;background:rgba(120,120,120,.55);color:#ddd}

/* service strip */
.strip{left:0;top:544px;width:1200px;height:89px;background:var(--navy)}
.strip .item{position:absolute;top:16px;transform:translateX(-50%);text-align:center;color:#fff;font-family:var(--body);font-size:13.5px;letter-spacing:.5px;white-space:nowrap}
.strip .item svg{margin:0 auto 8px}

/* intro */
.form-card{left:150px;top:709px;width:266px;height:370px;background:var(--light);box-shadow:0 0 0 5px #fff,0 2px 10px rgba(0,0,0,.12)}
.form-card h3{position:absolute;top:24px;width:100%;text-align:center;font-family:var(--head);color:var(--navy-deep);font-size:16px}
.form-card .sub{position:absolute;top:50px;left:30px;width:206px;text-align:center;font-size:10.5px;color:var(--muted);line-height:13px}
.field{position:absolute;left:20px;width:226px;height:28px;background:#fff;font-size:10.5px;color:#999;display:flex;align-items:center;gap:8px;padding-left:9px}
.form-card .msg{height:60px;align-items:flex-start;padding-top:9px}
.form-card .legal{position:absolute;top:277px;left:25px;width:216px;text-align:center;font-size:9.5px;color:var(--muted);line-height:12px}
.form-card .send{position:absolute;top:318px;left:94px;width:78px;height:27px;background:var(--navy)}
.intro{left:492px;top:730px;width:520px}
.intro h2{font-family:var(--head);color:var(--navy);font-size:23px;line-height:30px;font-weight:700}
.intro h4{margin-top:8px;font-family:var(--head);color:var(--navy);font-size:12.5px;font-weight:700}
.intro p{margin-top:18px;font-size:12px;line-height:16px;color:#333}

/* testimonials */
.reviews{left:0;top:1157px;width:1200px;height:499px;background:var(--navy-deep)}
.reviews h2{position:absolute;top:70px;width:100%;text-align:center;font-family:var(--head);color:#fff;font-size:22px;font-weight:700;letter-spacing:.3px}
.reviews h3{position:absolute;top:101px;width:100%;text-align:center;font-family:var(--head);color:#fff;font-size:14.5px;font-weight:700}
.quote-icon{left:150px;top:1305px;width:56px;height:56px;border-radius:50%;background:#fff;display:flex;align-items:center;justify-content:center}
.quote{left:150px;top:1372px;width:555px;color:#fff;font-size:13px;line-height:18.2px}
.author{left:150px;top:1538px;display:flex;align-items:center;gap:10px}
.author .avatar{width:46px;height:46px;border-radius:50%;background:linear-gradient(135deg,#6b4e3e,#2f2420);border:2px solid #ccc}
.author b{display:block;color:#fff;font-size:12.5px}
.author span{color:#7fb3d1;font-size:11px}
.dots{left:383px;top:1561px;display:flex;gap:7px}
.dots i{width:8px;height:8px;border:1px solid #777;border-radius:50%}
.dots i.on{width:11px;height:11px;margin-top:-1.5px;border-color:#ccc}
.view-all{left:557px;top:1549px;width:96px;height:30px;background:var(--navy)}
.award-card{left:750px;top:1310px;width:301px;height:266px;background:var(--steel);color:#fff;text-align:center}
.award-card .badge{margin:50px auto 0;width:156px;height:36px;background:#c9252f;border-radius:2px}
.award-card p{position:absolute;top:123px;left:32px;width:237px;font-size:12.5px;line-height:18.2px}

/* evaluate */
.eval-photo{left:0;top:1656px;width:625px;height:342px;background:linear-gradient(120deg,#8a5a3c 0%,#c9ad93 40%,#3f4a5c 70%,#d7d2cc 100%)}
.eval{left:625px;top:1656px;width:575px;height:342px;background:var(--grey)}
.eval h2{position:absolute;left:70px;top:70px;font-family:var(--head);color:var(--navy);font-size:22.5px;line-height:28px;font-weight:700}
.eval p{position:absolute;left:70px;top:138px;width:300px;font-size:12px;line-height:16.5px;color:#333}
.eval .go{position:absolute;left:70px;top:245px;width:206px;height:28px}

/* practice areas */
.pa-title{left:0;top:2068px;width:1200px;text-align:center;font-family:var(--head);color:var(--navy);font-size:23px;font-weight:700}
.pa-lead{left:280px;top:2110px;width:640px;text-align:center;font-size:12.5px;line-height:17px;color:#333}
.card{position:absolute;top:2200px;width:206px;height:215px;background:#fff;box-shadow:0 2px 14px rgba(0,0,0,.09);text-align:center}
.card .icon{position:absolute;left:64px;top:-28px;width:78px;height:78px;border-radius:50%;background:var(--navy);border:5px solid #fff;box-shadow:0 2px 8px rgba(0,0,0,.15);display:flex;align-items:center;justify-content:center}
.card h4{position:absolute;top:83px;width:100%;font-family:var(--head);font-size:13.5px;color:var(--navy);font-weight:700;line-height:17px}
.card p{position:absolute;top:118px;left:14px;width:178px;font-size:11px;line-height:14.5px;color:var(--muted)}
.card.two h4{top:74px}
.scroll{left:200px;top:2454px;width:800px;height:6px;background:#fff;box-shadow:0 1px 4px rgba(0,0,0,.15)}
.scroll i{position:absolute;left:166px;top:1px;width:542px;height:4px;background:var(--navy)}

/* results */
.results-left{left:0;top:2531px;width:681px;height:473px;background:var(--grey)}
.results-right{left:681px;top:2531px;width:519px;height:473px;background:var(--navy)}
.results h2{position:absolute;left:150px;top:2626px;font-family:var(--head);color:var(--navy);font-size:23px;line-height:27.5px;font-weight:700}
.results h4{position:absolute;left:150px;top:2728px;font-family:var(--head);color:var(--navy);font-size:14.5px;font-weight:700}
.results p{position:absolute;left:150px;top:2758px;width:345px;font-size:11.5px;line-height:15.5px;color:#333}
.stat{position:absolute;top:2827px;width:163px;height:77px;background:#fff;box-shadow:0 2px 8px rgba(0,0,0,.1);padding:20px 0 0 24px}
.stat b{display:block;font-family:var(--head);color:var(--navy);font-size:18px}
.stat span{font-size:11px;color:var(--navy);letter-spacing:.3px}
.video-frame{left:570px;top:2607px;width:478px;height:321px;background:radial-gradient(ellipse at 55% 55%,#6a5546 0%,#3a2f29 55%,#1f1a18 100%);border:2px solid #fff}
.play{position:absolute;left:207px;top:129px;width:62px;height:62px;border-radius:50%;background:var(--navy);display:flex;align-items:center;justify-content:center}

/* awards */
.aw-title{left:0;top:3072px;width:1200px;text-align:center;font-family:var(--head);color:var(--navy);font-size:22.5px;font-weight:700;letter-spacing:.3px}
.aw-badge{position:absolute;top:3134px;height:50px}

/* footer */
.footer{left:0;top:3383px;width:1200px;height:301px;background:linear-gradient(180deg,#1a242c,#0f171d)}
.cta{left:273px;top:3263px;width:655px;height:167px;background:#fff;box-shadow:0 4px 16px rgba(0,0,0,.15)}
.cta .photo{position:absolute;left:4px;top:4px;width:273px;height:159px;background:linear-gradient(120deg,#4a5160 0%,#c8b39c 50%,#e6e2dd 100%)}
.cta h2{position:absolute;left:318px;top:44px;font-family:var(--head);color:var(--navy-deep);font-size:26px;line-height:36px;font-weight:700}
.cta .arrow{position:absolute;left:568px;top:50px;width:56px;height:66px;background:var(--navy);display:flex;align-items:center;justify-content:center}
.f-brand{left:150px;top:3483px;display:flex;align-items:center;gap:8px}
.f-brand .mark{width:32px;height:32px;border:2px solid #d8d8d8;flex:none}
.f-brand .name{font-family:var(--head);font-size:13px;letter-spacing:3px;color:#d8d8d8;line-height:1.2;white-space:nowrap}
.f-about{left:150px;top:3535px;width:215px;color:#ddd;font-size:10.5px;line-height:13.5px}
.f-h{font-family:var(--head);font-size:13.5px;color:#3d8fbb;font-weight:700}
.f-col{color:#ddd;font-size:10.5px;line-height:14px}
.f-row{display:flex;gap:8px;align-items:flex-start}
.links{left:898px;top:3516px;color:#ddd;font-size:11px;line-height:19.4px}
.links .dim{color:#555}
.bottom{left:0;top:3684px;width:1200px;height:40px;background:var(--navy);color:#fff;font-size:11px}
.bottom .copy{position:absolute;left:150px;top:14px}
.social{position:absolute;left:916px;top:14px;display:flex;gap:20px}
.social i{width:12px;height:12px;border-radius:50%;background:#fff}
</style>
</head>
<body>

<!-- top bar -->
<div class="abs topbar">
  <div class="abs contact">
    <span><svg width="11" height="11" viewBox="0 0 24 24"><path fill="#fff" d="M6.6 10.8a15 15 0 0 0 6.6 6.6l2.2-2.2c.3-.3.7-.4 1-.2 1.1.4 2.3.6 3.6.6.6 0 1 .4 1 1V20c0 .6-.4 1-1 1A17 17 0 0 1 3 4c0-.6.4-1 1-1h3.5c.6 0 1 .4 1 1 0 1.3.2 2.5.6 3.6.1.3 0 .7-.2 1z"/></svg>555.010.2040</span>
    <span><svg width="11" height="11" viewBox="0 0 24 24"><path fill="none" stroke="#fff" stroke-width="2.5" d="M3 6h18v12H3zM3 6l9 7 9-7"/></svg>daniel@dorvantlegal.ca</span>
  </div>
  <div class="abs region">GTA - HAMILTON - NIAGARA</div>
  <div class="abs search"><svg width="11" height="11" viewBox="0 0 24 24"><circle cx="10" cy="10" r="6" fill="none" stroke="#fff" stroke-width="2.5"/><path d="M15 15l6 6" stroke="#fff" stroke-width="2.5"/></svg></div>
</div>

<!-- header -->
<header class="abs header">
  <div class="abs brand"><div class="mark"></div><div class="name">DORVANT<br>LAW FIRM</div></div>
  <div class="abs tagline">"Getting the results that matter!"</div>
  <nav class="abs nav"><span class="active">PRACTICE AREAS</span><span>ABOUT</span><span>NEWS</span><span>RESOURCES</span><span>CONTACT</span></nav>
  <div class="abs cta-btn">BOOK A CONSULTATION!</div>
</header>

<!-- hero -->
<section class="abs hero" role="img" aria-label="Dimly lit law office with scales of justice in the background">
  <div class="abs hero-portrait" role="img" aria-label="Portrait of the lead lawyer in a dark suit and red tie"></div>
  <h1 class="abs">WINNING.<br>MY CLIENTS DEPEND<br>ON ME FOR IT.<br>SHOULDN'T YOU?</h1>
  <div class="abs btn read">READ MORE</div>
  <div class="abs btn video">VIDEO LIBRARY</div>
</section>

<!-- service strip -->
<section class="abs strip">
  <div class="item" style="left:306px"><svg width="34" height="30" viewBox="0 0 34 30"><rect x="3" y="9" width="24" height="16" rx="2" fill="#fff"/><rect x="11" y="4" width="8" height="6" fill="none" stroke="#fff" stroke-width="2"/><path d="M22 20l9 9" stroke="#fff" stroke-width="3"/></svg>BUSINESS LAW</div>
  <div class="item" style="left:480px"><svg width="34" height="30" viewBox="0 0 34 30"><path d="M17 2l10 4v8c0 7-5 11-10 14C12 25 7 21 7 14V6z" fill="none" stroke="#fff" stroke-width="2.5"/><path d="M12 15l4 4 7-8" fill="none" stroke="#fff" stroke-width="2.5"/></svg>INSURANCE</div>
  <div class="item" style="left:661px"><svg width="34" height="30" viewBox="0 0 34 30"><path d="M17 16s-8-5-8-10a4 4 0 0 1 8-1 4 4 0 0 1 8 1c0 5-8 10-8 10z" fill="#fff"/><path d="M3 22h8l6 3 12-5v4l-12 5-8-3H3z" fill="#fff"/></svg>MALPRACTICE</div>
  <div class="item" style="left:872px"><svg width="34" height="30" viewBox="0 0 34 30"><path d="M4 3h20v15H12l-6 5v-5H4z" fill="#fff"/><path d="M26 9h4v14h-3v4l-5-4h-8v-3" fill="none" stroke="#fff" stroke-width="2"/></svg>PERSONAL INQUIRY</div>
</section>

<!-- case evaluation form -->
<div class="abs form-card">
  <h3>CASE EVALUATION</h3>
  <div class="sub">Fill out this form to schedule your initial consult with our lawyers.</div>
  <div class="field" style="top:93px">Name</div>
  <div class="field" style="top:131px">Email</div>
  <div class="field" style="top:168px">Phone</div>
  <div class="field msg" style="top:206px">Message</div>
  <div class="legal">* By using this site and/or submitting this form, I agree to the Privacy Policy and Terms of Use.</div>
  <div class="btn send">SEND</div>
</div>

<div class="abs intro">
  <h2>YOUR EXPERIENCED TORONTO<br>AND HAMILTON LAWYERS</h2>
  <h4>GETTING THE RESULTS THAT MATTER</h4>
  <p style="margin-top:26px">Dorvant Law Firm is a boutique litigation firm with law offices in Toronto and Hamilton. We concentrate our legal practice on complex business litigation, professional negligence (malpractice) claims, commercial contracts, and insurance coverage disputes.</p>
  <p>We take an innovative approach to our client's legal problems, and are guided by the philosophy that our job is to get results.</p>
  <p>The lawyers at Dorvant Law Firm have the reputation for vigorously representing their clients' interests and competing hard to obtain the best possible results. With experience at all stages of legal disputes, the lawyers at Dorvant Law Firm are equally at home negotiating in a boardroom or presenting a case at trial.</p>
  <p>We hope that you take the time to explore our website to find out how our record of excellence, expertise and many years of experience can assist you.</p>
</div>

<!-- testimonials -->
<section class="abs reviews">
  <h2>PEER RATED BY FELLOW LAWYERS FOR HIGH ACHIEVEMENT</h2>
  <h3>AND FURTHER QUALIFIED FROM CLIENT TESTIMONIALS</h3>
</section>
<div class="abs quote-icon"><svg width="26" height="22" viewBox="0 0 26 22"><path d="M2 10c0-5 3-8 8-9v4c-2 1-3 2-3 4h3v10H2zM15 10c0-5 3-8 8-9v4c-2 1-3 2-3 4h3v10h-8z" fill="#0b3954"/></svg></div>
<p class="abs quote">I cannot say enough about having Daniel Varro as my lawyer! I found him during a very difficult and stressful time and was so nervous about finding a good lawyer after having a few bad experiences. The experience that I had with Daniel eased ALL of that anxiety for me! He worked very very hard on my settlement and was very reassuring and truly cared about my situation. I always knew what was going on with my case as he always kept me updated with phone calls, emails and everything that was pertained to my case… I highly recommend Daniel Varro as a lawyer and if you know someone who is thorough and who truly cares about your case and you as a person than this is the man to go to!!!</p>
<div class="abs author"><div class="avatar" role="img" aria-label="Client portrait"></div><div><b>Nora Whitfield</b><span>Litigation Client</span></div></div>
<div class="abs dots"><i></i><i></i><i class="on"></i><i></i><i></i></div>
<div class="abs btn view-all">VIEW ALL</div>
<div class="abs award-card">
  <div class="badge"></div>
  <p>An excellent rating for a lawyer with some experience. This rating indicates the attorney is widely respected by their peers for high professional achievement and ethical standards.</p>
</div>

<!-- evaluate -->
<div class="abs eval-photo" role="img" aria-label="Team of lawyers meeting with clients around a table"></div>
<section class="abs eval">
  <h2>HAVE A CASE? LETS<br>EVALUATE IT.</h2>
  <p>Lorem Ipsum is simply dummy text of the printing and typesetting industry. Lorem Ipsum has been the industry's standard dummy text ever since the 1500s, when an unknown printer took a galley of type and scrambled it to make a type specimen book.</p>
  <div class="btn go" style="background:var(--navy)">LET'S EVALUATE YOUR CASE</div>
</section>

<!-- practice areas -->
<h2 class="abs pa-title">PRACTICE AREAS</h2>
<p class="abs pa-lead">Lorem Ipsum is simply dummy text of the printing and typesetting industry. Lorem Ipsum has been the industry's standard dummy text ever since the 1500s, when an unknown…</p>

<div class="card" style="left:46px"><div class="icon"><svg width="34" height="30" viewBox="0 0 34 30"><rect x="3" y="9" width="24" height="16" rx="2" fill="#fff"/><rect x="11" y="4" width="8" height="6" fill="none" stroke="#fff" stroke-width="2"/><path d="M22 20l9 9" stroke="#fff" stroke-width="3"/></svg></div><h4>BUSINESS LAW</h4><p>Business disputes can have a serious impact upon your company's bottom line.</p></div>
<div class="card" style="left:272px"><div class="icon"><svg width="34" height="30" viewBox="0 0 34 30"><path d="M17 2l10 4v8c0 7-5 11-10 14C12 25 7 21 7 14V6z" fill="none" stroke="#fff" stroke-width="2.5"/><path d="M12 15l4 4 7-8" fill="none" stroke="#fff" stroke-width="2.5"/></svg></div><h4>INSURANCE</h4><p>When your insurance company refuses to pay, you need a lawyer who has experience suing insurance companies, and winning</p></div>
<div class="card" style="left:497px"><div class="icon"><svg width="34" height="30" viewBox="0 0 34 30"><path d="M17 16s-8-5-8-10a4 4 0 0 1 8-1 4 4 0 0 1 8 1c0 5-8 10-8 10z" fill="#fff"/><path d="M3 22h8l6 3 12-5v4l-12 5-8-3H3z" fill="#fff"/></svg></div><h4>MALPRACTICE</h4><p>When a professional has let you down, the impact can be devastating. I have the experience need to help.</p></div>
<div class="card" style="left:721px"><div class="icon"><svg width="34" height="30" viewBox="0 0 34 30"><path d="M4 3h20v15H12l-6 5v-5H4z" fill="#fff"/><path d="M26 9h4v14h-3v4l-5-4h-8v-3" fill="none" stroke="#fff" stroke-width="2"/></svg></div><h4>CONTRACT DISPUTES</h4><p>When a partner breaks a deal, the impact can be devastating. I have the experience need to help.</p></div>
<div class="card two" style="left:947px"><div class="icon"><svg width="34" height="32" viewBox="0 0 34 32"><circle cx="14" cy="16" r="8" fill="none" stroke="#fff" stroke-width="5" stroke-dasharray="4 2.3"/><circle cx="14" cy="16" r="3" fill="#fff"/><path d="M25 4v24M22 4h6" stroke="#fff" stroke-width="3"/></svg></div><h4>OTHER LEGAL<br>SERVICES</h4><p>Lorem Ipsum is simply dummy text of the printing and typesetting industry. Lorem Ipsum has been the industry's standard…</p></div>
<div class="abs scroll"><i></i></div>

<!-- results -->
<div class="abs results-left"></div>
<div class="abs results-right"></div>
<section class="results">
  <h2>TORONTO'S RESULTS<br>FOCUSED BUSINESS LAW<br>FIRM</h2>
  <h4>SOMETHING CATCHY HERE</h4>
  <p>Lorem Ipsum is simply dummy text of the printing and typesetting industry. Lorem Ipsum has been the industry's standard dummy text ever since</p>
  <div class="stat" style="left:150px"><b>17+ YEARS</b><span>OF LITIGATION</span></div>
  <div class="stat" style="left:330px"><b>HUNDREDS</b><span>OF CASES WON</span></div>
</section>
<div class="abs video-frame" role="img" aria-label="Video still of a lawyer arguing in a courtroom">
  <div class="play"><svg width="22" height="24" viewBox="0 0 22 24"><path d="M3 2l17 10L3 22z" fill="#fff"/></svg></div>
</div>

<!-- awards -->
<h2 class="abs aw-title">PEERLINE REVIEW AWARD</h2>
<div class="aw-badge" style="left:291px;width:178px;background:#c9252f;top:3142px;height:42px"></div>
<div class="aw-badge" style="left:536px;width:136px;"><svg width="136" height="50" viewBox="0 0 136 50"><circle cx="22" cy="25" r="19" fill="#2d6f9c"/><rect x="48" y="17" width="84" height="16" rx="2" fill="#b9c9d6"/></svg></div>
<div class="aw-badge" style="left:730px;width:180px;"><svg width="180" height="50" viewBox="0 0 180 50"><rect x="2" y="4" width="40" height="42" rx="6" fill="#1d3f7a"/><rect x="54" y="14" width="122" height="22" rx="2" fill="#c8d3e3"/></svg></div>

<!-- footer -->
<footer class="abs footer"></footer>
<div class="abs cta">
  <div class="photo" role="img" aria-label="Colleagues reviewing documents together"></div>
  <h2>LET'S WORK<br>TOGETHER</h2>
  <div class="arrow"><svg width="20" height="18" viewBox="0 0 20 18"><path d="M1 9h16M10 2l7 7-7 7" fill="none" stroke="#fff" stroke-width="2"/></svg></div>
</div>

<div class="abs f-brand"><div class="mark"></div><div class="name">DORVANT<br>LAW FIRM</div></div>
<p class="abs f-about">Dorvant Law Firm is a boutique law office concentrating in Complex Business Litigation, Professional Negligence, Commercial Contracts, and Insurance Coverage Disputes. Our innovative and pugnacious approach gets results for our clients in the Greater Toronto Area. HST #100000000RT0001</p>

<div class="abs f-h" style="left:447px;top:3484px">CONTACT INFO</div>
<div class="abs f-col" style="left:447px;top:3522px">
  <div class="f-row" style="margin-bottom:18px"><svg width="12" height="12" viewBox="0 0 24 24"><path fill="#3d8fbb" d="M6.6 10.8a15 15 0 0 0 6.6 6.6l2.2-2.2c.3-.3.7-.4 1-.2 1.1.4 2.3.6 3.6.6.6 0 1 .4 1 1V20c0 .6-.4 1-1 1A17 17 0 0 1 3 4c0-.6.4-1 1-1h3.5c.6 0 1 .4 1 1 0 1.3.2 2.5.6 3.6.1.3 0 .7-.2 1z"/></svg><span style="margin-left:2px">555.010.2040</span></div>
  <div class="f-row" style="margin-bottom:16px"><svg width="12" height="12" viewBox="0 0 24 24"><path fill="#3d8fbb" d="M2 5h20v14H2z"/></svg><span style="margin-left:2px">daniel@dorvantlegal.ca</span></div>
  <div class="f-row"><svg width="12" height="14" viewBox="0 0 24 28"><path fill="#3d8fbb" d="M12 0a9 9 0 0 1 9 9c0 7-9 19-9 19S3 16 3 9a9 9 0 0 1 9-9z"/></svg><div style="margin-left:2px"><b>Hamilton Office:</b><br>45 Ridge Street E, Ground Floor<br>Hamilton, ON L8N 0B2</div></div>
</div>
<div class="abs f-col" style="left:651px;top:3522px">
  <div class="f-row" style="margin-bottom:16px"><svg width="12" height="14" viewBox="0 0 24 28"><path fill="#3d8fbb" d="M12 0a9 9 0 0 1 9 9c0 7-9 19-9 19S3 16 3 9a9 9 0 0 1 9-9z"/></svg><div style="margin-left:2px"><b>Toronto Office:</b><br>200 Harbour Lane, Suite 410,<br>Toronto, ON M5X 0A1</div></div>
  <div class="f-row"><svg width="12" height="14" viewBox="0 0 24 28"><path fill="#3d8fbb" d="M12 0a9 9 0 0 1 9 9c0 7-9 19-9 19S3 16 3 9a9 9 0 0 1 9-9z"/></svg><div style="margin-left:2px"><b>Niagara Office:</b><br>12 Orchard Way, Virgil,<br>ON L0S 0A3</div></div>
</div>

<div class="abs f-h" style="left:898px;top:3484px">QUICK LINK</div>
<div class="abs links"><div class="dim">Home</div><div>Practice Areas</div><div>About</div><div>News</div><div>Resources</div><div>Contact</div></div>

<div class="abs bottom">
  <div class="copy">© 2023 Dorvant Law Firm. All Rights Reserved.</div>
  <div class="social"><i></i><i></i><i></i></div>
</div>

</body>
</html>
```